VARNO - new private security company in Guyana, South America needs a website & logo design

New private security company in Guyana needs a website ready for the company launch. The business will offer armed and unarmed security to high net worth individuals, politicians, government officials, diplomats and off-shore oil industry vessels and platforms.

The company has its own heliport and indoor training range, armoured vehicles, ambulances and uniformed security personnel, and we would like some imager to indicate this.

The team leaders are all ex-special forces.

The website structure should be something like:

PAGE 1 Home
PAGE 2 About Us
PAGE 3 Guyana Security Overview
PAGE 4 Services
PAGE 5 Contact Us
PAGE 6 Useful Links

We have uploaded a file with the text copy for each of these pages.

The web domain has been registered through 456-dom and is www.varno.group

Target Market(s)

Corporations involved in the oil and gas industry, Embassies, Investment companies and individuals, Caribbean diaspora.

Industry/Entity Type

Security Service

Logo Text

VARNO

Coding

Coded - Design and coding required

Number of Pages Required

5+ page

Font styles to use
Sans Serif

Requirements
Must have
• Must have:
an enquiry/contact form page
general location map: https://mapz.example/loc/kP8wq2Lbnxv7hRt4;
text as per web content document uploaded to this site
Nice to have
• Images of private security (cars, bodyguards, helicopters/planes, etc)
Images of Maritime security (non-military)
Images of people of colour (Guyana has mainly afro and indian residents)
Image of a high tec security control room

```html
<!DOCTYPE html>
<html lang="en">
<head>
<meta charset="utf-8">
<title>VARNO – Private Security Guyana</title>
<link href="https://fonts.googleapis.com/css2?family=Roboto:wght@300;400;500;700&display=swap" rel="stylesheet">
<style>
:root{
  --blue:#1f9fe0;
  --blue-soft:rgba(31,159,224,.78);
  --ink:#1d2026;
  --dark:#16191f;
  --grey-text:#6d737c;
  --light:#f4f5f7;
  --line:#e3e6ea;
  --white:#ffffff;
}
*{box-sizing:border-box;margin:0;padding:0}
html,body{width:1200px;height:5128px;overflow:hidden}
body{font-family:'Roboto',Arial,sans-serif;color:var(--ink);background:var(--white);position:relative}
a{color:inherit;text-decoration:none}
.btn{display:inline-block;background:var(--ink);color:var(--white);font-size:12px;font-weight:500;letter-spacing:1px;padding:12px 28px;border-radius:22px}
.section-title{text-align:center;font-size:40px;font-weight:700;color:var(--ink)}
.section-title span{color:var(--blue)}
.title-bar{width:60px;height:3px;background:var(--blue);margin:14px auto 18px}
.section-lead{text-align:center;font-size:15px;line-height:1.5;color:var(--grey-text);width:560px;margin:0 auto}

/* top + hero */
.hero{position:absolute;top:0;left:0;width:1200px;height:740px;background:linear-gradient(100deg,#1c2a38 0%,#2a3e52 45%,#15202b 100%)}
.hero-photo{position:absolute;inset:0;background:radial-gradient(ellipse at 25% 35%,rgba(120,140,160,.35),transparent 60%),linear-gradient(180deg,rgba(0,0,0,.1),rgba(0,0,0,.45))}
.topbar{position:absolute;top:0;left:0;width:1200px;height:48px;background:rgba(10,12,16,.75);display:flex;align-items:center;padding:0 60px;color:#cfd4da;font-size:13px;gap:34px}
.topbar .item{display:flex;align-items:center;gap:8px}
.topbar .social{margin-left:auto;display:flex;gap:10px}
.topbar .social i{width:14px;height:14px;background:#9aa2ab;display:block;border-radius:2px}
.navbar{position:absolute;top:62px;left:60px;right:40px;height:56px;display:flex;align-items:center}
.brand{display:flex;align-items:center;gap:10px;color:var(--white);font-size:32px;font-weight:700;letter-spacing:1px}
.brand .dot{width:34px;height:34px;border-radius:50%;background:var(--blue)}
.nav{margin-left:auto;display:flex;gap:30px;font-size:13px;font-weight:500;color:var(--white);letter-spacing:.5px}
.nav .active{color:var(--blue)}
.hero-text{position:absolute;top:232px;left:68px;color:var(--white)}
.hero-text h1{font-size:56px;font-weight:400;line-height:1.12}
.hero-text h1 span{color:var(--blue)}
.hero-text p{margin-top:34px;width:360px;font-size:15px;line-height:1.6;color:#d6dbe1}
.hero-text .btn{margin-top:40px}
.feature-boxes{position:absolute;top:620px;left:68px;display:flex;gap:40px}
.feature{width:334px;height:268px;background:var(--blue-soft);color:var(--white);text-align:center;padding-top:92px}
.feature h3{font-size:16px;font-weight:500;letter-spacing:.5px}
.feature p{font-size:13px;margin-top:6px;opacity:.9}

/* why */
.why{position:absolute;top:960px;left:0;width:1200px;height:592px}
.why .section-title{text-align:left;position:absolute;left:68px;top:20px}
.why .title-bar{position:absolute;left:68px;top:76px;margin:0}
.why-list{position:absolute;left:68px;top:120px;width:500px}
.why-item{display:flex;gap:26px;margin-bottom:44px}
.why-item svg{flex:none;margin-top:4px}
.why-item h4{font-size:16px;font-weight:500;margin-bottom:8px}
.why-item p{font-size:14px;line-height:1.55;color:var(--grey-text)}
.why-photo{position:absolute;left:612px;top:120px;width:520px;height:372px;background:linear-gradient(135deg,#dfe6ee,#8fa2b6 55%,#2b3a4c)}
.play{position:absolute;left:226px;top:148px;width:64px;height:64px;border-radius:50%;background:var(--blue);display:flex;align-items:center;justify-content:center}

/* services */
.services{position:absolute;top:1552px;left:0;width:1200px;height:1068px;background:linear-gradient(180deg,#1a1e24,#232931 50%,#1a1e24)}
.services .section-title{color:var(--white);margin-top:92px}
.services .section-lead{color:#c9ced5}
.service-grid{position:absolute;top:268px;left:68px;width:1064px;display:grid;grid-template-columns:repeat(3,1fr);border-top:1px solid rgba(255,255,255,.15);border-left:1px solid rgba(255,255,255,.15)}
.service{height:360px;border-right:1px solid rgba(255,255,255,.15);border-bottom:1px solid rgba(255,255,255,.15);text-align:center;color:var(--white);padding-top:58px}
.service svg{display:block;margin:0 auto 24px}
.service h3{font-size:17px;font-weight:700;line-height:1.35;width:260px;margin:0 auto}
.service p{font-size:13px;color:#8f97a1;line-height:1.5;width:220px;margin:14px auto 16px}
.service .more{font-size:13px;color:var(--blue);font-weight:500}

/* testimonial */
.testimonial{position:absolute;top:2620px;left:0;width:1200px;height:580px;background:linear-gradient(120deg,#1f3346,#2c4a64 55%,#1e2f40)}
.testimonial .section-title{color:var(--white);margin-top:100px}
.testimonial .section-lead{color:#d3d9e0}
.quote{position:absolute;top:300px;left:80px;display:flex;gap:28px;color:var(--white)}
.avatar{width:136px;height:136px;border-radius:50%;background:linear-gradient(160deg,#e9ecef,#9aa7b4);border:4px solid #fff;flex:none}
.quote p{font-size:14px;line-height:1.6;width:620px;margin-top:22px}
.quote h5{font-size:14px;font-weight:500;margin-top:12px}
.quote small{font-size:13px;color:#aeb8c3}
.dots{display:flex;gap:10px;justify-content:center}
.dots i{width:10px;height:10px;border-radius:50%;background:#9aa3ad;display:block}
.dots i.on{background:var(--white)}
.testimonial .dots{position:absolute;top:500px;left:0;right:0}

/* banner */
.banner{position:absolute;top:3200px;left:0;width:1200px;height:272px;background:linear-gradient(90deg,#2a8fcb,#47aee3 60%,#2f99d4)}
.banner h2{position:absolute;left:68px;top:96px;font-size:38px;font-weight:400;line-height:1.2;color:var(--white)}
.banner h2 b{font-weight:700;color:#0f2c44}
.banner .btn{position:absolute;right:150px;top:104px}

/* blog */
.blog{position:absolute;top:3472px;left:0;width:1200px;height:1068px;background:var(--light)}
.blog .section-title{margin-top:200px}
.blog-cards{position:absolute;top:420px;left:68px;display:flex;gap:34px}
.card{width:332px;height:350px;background:var(--white);text-align:center}
.card .thumb{height:216px}
.card h3{font-size:16px;font-weight:500;margin:18px 0 8px}
.card p{font-size:12px;line-height:1.45;color:var(--grey-text);width:270px;margin:0 auto 12px}
.card .btn{padding:8px 22px;font-size:11px}
.partners{position:absolute;top:820px;left:68px;display:flex;gap:40px}
.partner{width:180px;height:110px;background:var(--white);display:flex;align-items:center;justify-content:center}
.partner span{width:96px;height:30px;background:#d9dde2;border-radius:3px;display:block}
.blog .dots{position:absolute;top:990px;left:0;right:0}
.blog .dots i{background:#c5cbd2}
.blog .dots i.on{background:var(--blue)}

/* footer */
.footer{position:absolute;top:4540px;left:0;width:1200px;height:588px;background:var(--dark);color:#aeb4bc}
.footer-cols{position:absolute;top:100px;left:68px;display:flex;gap:0}
.fcol{width:274px}
.fcol h4{color:var(--white);font-size:14px;font-weight:700;letter-spacing:.8px;margin-bottom:30px}
.fcol li{list-style:none;font-size:13px;margin-bottom:22px}
.fcol p{font-size:13px;line-height:1.6;margin-bottom:20px;width:230px}
.fcol .ci{display:flex;align-items:center;gap:10px;font-size:13px;margin-bottom:20px}
.footer-bottom{position:absolute;left:68px;right:68px;top:470px;height:80px;border-top:1px solid #2a2f37;display:flex;align-items:center}
.footer-bottom .brand{font-size:28px}
.footer-bottom .brand .dot{width:30px;height:30px}
.legal{margin-left:auto;display:flex;gap:28px;font-size:12px;letter-spacing:.8px;color:#cfd4da}
</style>
</head>
<body>

<header class="hero">
  <div class="hero-photo" role="img" aria-label="Security officer in dark suit and sunglasses standing before a city background"></div>
  <div class="topbar">
    <span class="item"><svg width="16" height="12" viewBox="0 0 16 12"><rect x="0.5" y="0.5" width="15" height="11" fill="none" stroke="#cfd4da"/><path d="M1 1l7 6 7-6" fill="none" stroke="#cfd4da"/></svg>info@varno.group</span>
    <span class="item"><svg width="14" height="14" viewBox="0 0 24 24"><path d="M6.6 10.8a15 15 0 006.6 6.6l2.2-2.2a1 1 0 011-.25 11.4 11.4 0 003.6.6 1 1 0 011 1V20a1 1 0 01-1 1A17 17 0 013 4a1 1 0 011-1h3.5a1 1 0 011 1c0 1.25.2 2.45.6 3.6a1 1 0 01-.25 1z" fill="#cfd4da"/></svg>Call us : +592 2210-480</span>
    <span class="social"><i></i><i></i><i></i><i></i><i></i></span>
  </div>
  <nav class="navbar">
    <a class="brand" href="#"><span class="dot"></span>VARNO</a>
    <div class="nav">
      <a class="active" href="#">HOME</a><a href="#">ABOUT US</a><a href="#">GUYANA SECURITY OVERVIEW</a><a href="#">SERVICES</a><a href="#">CONTACT US</a><a href="#">USEFUL LINKS</a>
    </div>
  </nav>
  <div class="hero-text">
    <h1><span>Guyanese</span> Best Security<br>Around <span>You everytime.</span></h1>
    <p>Guard Team is a leader in the fields of common castsystems providing the latest in products and fields.</p>
    <a class="btn" href="#">READ MORE</a>
  </div>
</header>

<div class="feature-boxes">
  <div class="feature"><h3>PRIVATE SECURITY</h3><p>Tried &amp; Proven Security Guard Services</p></div>
  <div class="feature"><h3>DEFENSE TRAINING</h3><p>Tried &amp; Proven Security Guard Services</p></div>
  <div class="feature"><h3>GUARD HOUSE</h3><p>Tried &amp; Proven Security Guard Services</p></div>
</div>

<section class="why">
  <h2 class="section-title">Why Choose <span>Us</span></h2>
  <div class="title-bar"></div>
  <div class="why-list">
    <div class="why-item">
      <svg width="28" height="28" viewBox="0 0 28 28"><g stroke="#1f9fe0" stroke-width="2"><line x1="3" y1="7" x2="25" y2="7"/><line x1="3" y1="14" x2="25" y2="14"/><line x1="3" y1="21" x2="25" y2="21"/></g></svg>
      <div><h4>• Advanced Weapons Handling</h4><p>Strategic trained officers handle every firearm with care, keep each site under watch and report all activity to clients each day.</p></div>
    </div>
    <div class="why-item">
      <svg width="28" height="28" viewBox="0 0 24 24"><path d="M12 2l3 6.5 7 .8-5.2 4.8 1.4 7L12 17.6 5.8 21l1.4-7L2 9.3l7-.8z" fill="#1f9fe0"/></svg>
      <div><h4>Security Protocol</h4><p>Strategic clear protocols guide every shift, so teams act fast, stay alert and keep people and property safe at all times.</p></div>
    </div>
    <div class="why-item">
      <svg width="28" height="28" viewBox="0 0 24 24"><rect x="6" y="2" width="12" height="20" rx="2" fill="none" stroke="#1f9fe0" stroke-width="2"/><circle cx="12" cy="18" r="1" fill="#1f9fe0"/></svg>
      <div><h4>Support</h4><p>Strategic round the clock support keeps clients in touch with our control room and field leaders on any day of the week.</p></div>
    </div>
  </div>
  <div class="why-photo" role="img" aria-label="Uniformed security officer in cap and sunglasses speaking into a radio">
    <span class="play"><svg width="22" height="22" viewBox="0 0 22 22"><path d="M6 3l13 8-13 8z" fill="#fff"/></svg></span>
  </div>
</section>

<section class="services" role="region" aria-label="Services, over a dim photo of armed guards">
  <h2 class="section-title">Our <span>Services</span></h2>
  <div class="title-bar"></div>
  <p class="section-lead">Lorem ipsum dolor sit amet, consectetur adipiscing elit. Nostrum autem similique obcaecati non magni rerum maxime Officia.</p>
  <div class="service-grid">
    <div class="service">
      <svg width="36" height="36" viewBox="0 0 24 24"><path d="M4 5h16v11H4z M9 20h6 M12 16v4" fill="none" stroke="#1f9fe0" stroke-width="2"/></svg>
      <h3>Advanced Covert Surveillance (static &amp; mobile)</h3><p>Discreet watch on people and places, by day and night.</p><a class="more" href="#">Read More →</a>
    </div>
    <div class="service">
      <svg width="36" height="36" viewBox="0 0 24 24"><circle cx="12" cy="8" r="4" fill="#1f9fe0"/><path d="M4 21c0-4.4 3.6-7 8-7s8 2.6 8 7z" fill="#1f9fe0"/></svg>
      <h3>Kidnap &amp; Ransom Support</h3><p>Calm expert help for families and firms in a crisis.</p><a class="more" href="#">Read More →</a>
    </div>
    <div class="service">
      <svg width="36" height="36" viewBox="0 0 24 24"><rect x="3" y="7" width="18" height="13" rx="1" fill="#1f9fe0"/><rect x="9" y="3" width="6" height="4" fill="none" stroke="#1f9fe0" stroke-width="2"/></svg>
      <h3>Security Consultancy &amp; Advisory Services</h3><p>Risk reviews and plans built around each client.</p><a class="more" href="#">Read More →</a>
    </div>
    <div class="service">
      <svg width="36" height="36" viewBox="0 0 24 24"><path d="M12 2l8 3v6c0 5-3.4 9.4-8 11-4.6-1.6-8-6-8-11V5z" fill="#1f9fe0"/></svg>
      <h3>Personnel and Asset Tracking</h3><p>Live location data for staff, cargo and vehicles.</p><a class="more" href="#">Read More →</a>
    </div>
    <div class="service">
      <svg width="36" height="36" viewBox="0 0 24 24"><path d="M3 15h18l-3 5H6z M11 3v11 M11 4l7 8h-7" fill="#1f9fe0" stroke="#1f9fe0" stroke-width="1.5"/></svg>
      <h3>Maritime Security</h3><p>Protection for offshore vessels and oil platforms.</p><a class="more" href="#">Read More →</a>
    </div>
    <div class="service">
      <svg width="36" height="36" viewBox="0 0 24 24"><rect x="3" y="6" width="18" height="14" rx="1" fill="#1f9fe0"/><path d="M8 6V4h8v2" fill="none" stroke="#1f9fe0" stroke-width="2"/></svg>
      <h3>Security Training</h3><p>Range and field courses led by former special forces.</p><a class="more" href="#">Read More →</a>
    </div>
  </div>
</section>

<section class="testimonial">
  <h2 class="section-title">Our <span>Testimonial</span></h2>
  <div class="title-bar"></div>
  <p class="section-lead">Lorem ipsum dolor sit amet, consectetur adipiscing elit. Nostrum autem similique obcaecati non magni rerum maxime Officia.</p>
  <div class="quote">
    <div class="avatar" role="img" aria-label="Portrait of the client giving the testimonial"></div>
    <div>
      <p>Nam mattis dui ut nisi malesuada, vitae ullamcorper lectus vestibulum. Integer felis dui, ornare quis congue non, posuere in arcu. Nulla vivamus lectus ut felis auctor hendrerit. Aenean at lectus mauris. Cras viverra cursus nisl.</p>
      <h5>Marlon Reyes</h5>
      <small>CEO &amp; Founder | Ltd.</small>
    </div>
  </div>
  <div class="dots"><i class="on"></i><i></i><i></i></div>
</section>

<section class="banner" role="region" aria-label="Call to action over a blue tinted city photo">
  <h2>Delivering the Best <b>Security Solutions</b><br>to Our Clients.</h2>
  <a class="btn" href="#">MAKE APPOINTMENT</a>
</section>

<section class="blog">
  <h2 class="section-title">Our <span>Blog</span></h2>
  <div class="title-bar"></div>
  <p class="section-lead">Lorem ipsum dolor sit amet, consectetur adipiscing elit. Nostrum autem similique obcaecati non magni rerum maxime Officia.</p>
  <div class="blog-cards">
    <article class="card">
      <div class="thumb" role="img" aria-label="Police officer in uniform and sunglasses" style="background:linear-gradient(160deg,#6b7a8a,#2f3b48)"></div>
      <h3>Security Tips And Tactics</h3>
      <p>Sollicitudin lorem ipsum dolor sit amet, consectetur adipiscing elit. Duis sed odio sit amet nibh vulputate cursus.</p>
      <a class="btn" href="#">READ MORE</a>
    </article>
    <article class="card">
      <div class="thumb" role="img" aria-label="Female police officer in uniform in an office" style="background:linear-gradient(160deg,#b9a58f,#3b3a44)"></div>
      <h3>Business Security Tips Guide</h3>
      <p>Sollicitudin lorem ipsum dolor sit amet, consectetur adipiscing elit. Duis sed odio sit amet nibh vulputate cursus.</p>
      <a class="btn" href="#">READ MORE</a>
    </article>
    <article class="card">
      <div class="thumb" role="img" aria-label="Security cameras mounted on a wall under a blue sky" style="background:linear-gradient(180deg,#a9c6e4,#e6edf4)"></div>
      <h3>Benefits of a Security Guard</h3>
      <p>Sollicitudin lorem ipsum dolor sit amet, consectetur adipiscing elit. Duis sed odio sit amet nibh vulputate cursus.</p>
      <a class="btn" href="#">READ MORE</a>
    </article>
  </div>
  <div class="partners">
    <div class="partner"><span></span></div>
    <div class="partner"><span></span></div>
    <div class="partner"><span></span></div>
    <div class="partner"><span></span></div>
    <div class="partner"><span></span></div>
  </div>
  <div class="dots"><i class="on"></i><i></i></div>
</section>

<footer class="footer">
  <div class="footer-cols">
    <div class="fcol"><h4>AREAS SERVED</h4><ul><li>Commercial Security</li><li>Retail Security</li><li>Industrial Security</li><li>Consulting Security</li></ul></div>
    <div class="fcol"><h4>COMPANY</h4><ul><li>Press Releases</li><li>Mission</li><li>Strategy</li><li>Works</li></ul></div>
    <div class="fcol"><h4>ABOUT VARNO</h4><ul><li>Support</li><li>Loss Prevention</li><li>Customer Service</li><li>Event Security</li></ul></div>
    <div class="fcol"><h4>CONTACT US</h4>
      <p>Phasellus placerat rutrum tristique in fauce dictum.</p>
      <div class="ci"><svg width="14" height="14" viewBox="0 0 24 24"><path d="M6.6 10.8a15 15 0 006.6 6.6l2.2-2.2a1 1 0 011-.25 11.4 11.4 0 003.6.6 1 1 0 011 1V20a1 1 0 01-1 1A17 17 0 013 4a1 1 0 011-1h3.5a1 1 0 011 1c0 1.25.2 2.45.6 3.6a1 1 0 01-.25 1z" fill="#1f9fe0"/></svg>+592 2210-480</div>
      <div class="ci"><svg width="14" height="12" viewBox="0 0 16 12"><rect x="0.5" y="0.5" width="15" height="11" fill="none" stroke="#1f9fe0"/><path d="M1 1l7 6 7-6" fill="none" stroke="#1f9fe0"/></svg>info@varno.group</div>
      <div class="ci"><svg width="12" height="16" viewBox="0 0 12 16"><path d="M6 0a6 6 0 016 6c0 4.5-6 10-6 10S0 10.5 0 6a6 6 0 016-6z" fill="#1f9fe0"/><circle cx="6" cy="6" r="2" fill="#16191f"/></svg>18 Kessler Road, Georgetown, Guyana</div>
    </div>
  </div>
  <div class="footer-bottom">
    <a class="brand" href="#"><span class="dot"></span>VARNO</a>
    <div class="legal"><a href="#">PRIVACY POLICY</a><a href="#">TERMS &amp; CONDITIONS</a><a href="#">COPYRIGHT</a></div>
  </div>
</footer>

</body>
</html>
```